Tallowbrook Paws Postboardly Ad

Need to incorporate the logo
Special postboardly discount - get $50 off any package (the main focus of the ad)
First walk free
link to website: www.tallowbrookpaws.com
tag: "is your dog a tallowbrookpaws?
Target Market(s)
The target audience is dog owners in Burnaby with a household income of 100,000 plus. People that can afford dogs but because they are working full-time or long hours are not able to.
Font styles to use
Sans Serif
Colors
acd036
Requirements
Must have
- Focus on the $50 off any package

```html
<!DOCTYPE html>
<html lang="en">
<head>
<meta charset="utf-8">
<title>Tallowbrook Paws – Postboardly Ad</title>
<link rel="stylesheet" href="https://fonts.googleapis.com/css2?family=Archivo+Black&family=Josefin+Sans:wght@400&family=Oswald:wght@700&family=Tinos:wght@400;700&family=Open+Sans:wght@400&display=swap">
<style>
  :root {
    --brand-green: #acd036;
    --soft-green: #a9cc7a;
    --pale-green: #dfeec4;
    --ink: #231f20;
    --white: #ffffff;
    --stripe-text: #b6d27a;
  }
  * { margin: 0; padding: 0; box-sizing: border-box; }
  html, body { width: 1200px; height: 876px; overflow: hidden; background: var(--white); }
  .ad {
    position: relative; width: 1200px; height: 876px; overflow: hidden;
    background: var(--white); color: var(--ink);
  }
  .top-band {
    position: absolute; left: 0; top: 0; width: 1200px; height: 336px;
    background: radial-gradient(ellipse 380px 300px at 980px 150px, #ffffff 0%, #eef6dc 35%, var(--soft-green) 80%), var(--soft-green);
  }
  .puppy-photo {
    position: absolute; left: 760px; top: 40px; width: 440px; height: 340px;
    background: radial-gradient(ellipse 200px 150px at 230px 170px, #3a2f2a 0%, #6b4a36 45%, rgba(240,236,230,0.85) 78%, rgba(255,255,255,0) 100%);
  }
  .headline { position: absolute; left: 56px; top: 44px; z-index: 2; }
  .headline-lead {
    font-family: "Josefin Sans", sans-serif; font-weight: 400;
    font-size: 78px; line-height: 1; letter-spacing: 1px; color: var(--ink);
  }
  .headline-name {
    margin-top: 28px;
    font-family: "Archivo Black", sans-serif; font-size: 50px; line-height: 1;
    letter-spacing: 1px; color: var(--ink);
  }
  .discount {
    position: absolute; left: 62px; top: 262px; width: 286px; height: 310px;
    background: var(--white); border-radius: 22px; padding: 8px;
  }
  .discount-inner {
    width: 100%; height: 100%; background: var(--ink); border-radius: 16px;
    text-align: center; padding-top: 24px;
  }
  .discount-label {
    font-family: "Archivo Black", sans-serif; color: var(--soft-green);
    font-size: 17px; line-height: 1; white-space: nowrap;
  }
  .discount-title {
    font-family: "Archivo Black", sans-serif; color: var(--soft-green);
    font-size: 37px; line-height: 1; margin-top: 4px;
  }
  .discount-amount {
    position: absolute; left: 23px; top: 110px;
    font-family: "Oswald", sans-serif; font-weight: 700; color: var(--brand-green);
    font-size: 112px; line-height: 0.9; letter-spacing: -2px; white-space: nowrap;
    transform: scaleX(1.33); transform-origin: left top;
  }
  .discount-off {
    position: absolute; left: 121px; top: 210px;
    font-family: "Archivo Black", sans-serif; color: var(--white); font-size: 42px; line-height: 1;
  }
  .discount-package {
    position: absolute; left: 0; right: 0; top: 256px; text-align: center; white-space: nowrap;
    font-family: "Archivo Black", sans-serif; color: var(--white); font-size: 30px; line-height: 1;
  }
  .intro {
    position: absolute; left: 392px; top: 392px; width: 252px;
    font-family: "Tinos", serif; font-size: 22px; line-height: 27px; color: var(--ink);
  }
  .divider { position: absolute; left: 665px; top: 378px; width: 1px; height: 222px; background: var(--ink); }
  .features {
    position: absolute; left: 690px; top: 402px; list-style: none; white-space: nowrap;
    font-family: "Tinos", serif; font-size: 24px; line-height: 29px; color: var(--ink);
  }
  .features li { position: relative; padding-left: 30px; margin-bottom: 8px; }
  .features svg { position: absolute; left: 0; top: 5px; width: 20px; height: 20px; }
  .footer-stripe {
    position: absolute; left: 0; top: 707px; width: 1200px; height: 50px; background: var(--ink);
  }
  .footer-band {
    position: absolute; left: 0; top: 757px; width: 1200px; height: 119px; background: var(--soft-green);
  }
  .brand-name {
    position: absolute; left: 346px; top: 640px; white-space: nowrap;
    font-family: "Tinos", serif; font-weight: 700; font-size: 51px; line-height: 1; letter-spacing: 1px;
    color: var(--ink);
  }
  .brand-name .accent { color: var(--soft-green); }
  .tagline {
    position: absolute; left: 396px; top: 718px;
    font-family: "Open Sans", sans-serif; font-size: 25px; line-height: 1; color: var(--stripe-text);
    word-spacing: 2px;
  }
  .call {
    position: absolute; left: 358px; top: 782px; white-space: nowrap;
    font-family: "Archivo Black", sans-serif; font-size: 38px; line-height: 1; color: var(--ink);
  }
  .website {
    position: absolute; left: 388px; top: 823px; white-space: nowrap;
    font-family: "Archivo Black", sans-serif; font-size: 26px; line-height: 1; color: var(--white);
  }
  .logo { position: absolute; left: 50px; top: 612px; width: 262px; height: 236px; }
  .logo-mark {
    position: absolute; left: 88px; top: 8px; width: 86px; height: 86px;
    border-radius: 50%; background: var(--ink);
  }
  .logo-name {
    position: absolute; left: 6px; right: 6px; top: 150px; text-align: center; white-space: nowrap;
    font-family: "Archivo Black", sans-serif; font-size: 20px; line-height: 1; color: var(--ink);
    background: var(--white); padding: 12px 0; border-radius: 6px;
  }
  .seal { position: absolute; left: 948px; top: 632px; width: 230px; height: 230px; }
  .seal-text {
    position: absolute; left: 0; top: 0; width: 230px; height: 230px;
    display: flex; flex-direction: column; align-items: center; justify-content: center;
    font-family: "Archivo Black", sans-serif; color: var(--ink); line-height: 0.95;
    transform: rotate(-25deg);
  }
  .seal-text .small { font-size: 34px; }
  .seal-text .big { font-size: 50px; }
</style>
</head>
<body>
<main class="ad">
  <div class="top-band"></div>

  <div class="puppy-photo" role="img" aria-label="Photo of a tricolour spaniel puppy resting its paws on the edge of the white panel"></div>

  <header class="headline">
    <p class="headline-lead">IS YOUR DOG A</p>
    <h1 class="headline-name">TALLOWBROOK PAWS?</h1>
  </header>

  <section class="discount">
    <div class="discount-inner">
      <p class="discount-label">SPECIAL POSTBOARDLY</p>
      <p class="discount-title">DISCOUNT</p>
    </div>
    <p class="discount-amount">$50</p>
    <p class="discount-off">OFF</p>
    <p class="discount-package">ANY PACKAGE</p>
  </section>

  <p class="intro">Your Tallowbrook Paws requires sixty to ninety minutes of exercise a day. The reality of today’s busy lifestyle is that we can not always meet the needs of our beloved dog.</p>

  <div class="divider"></div>

  <ul class="features">
    <li><svg viewBox="0 0 18 18"><circle cx="9" cy="9" r="8" fill="#a9cc7a"/><path d="M4.5 9.5l3 3 6-7" stroke="#231f20" stroke-width="2.2" fill="none"/></svg>LICENSED AND INSURED.</li>
    <li><svg viewBox="0 0 18 18"><circle cx="9" cy="9" r="8" fill="#a9cc7a"/><path d="M4.5 9.5l3 3 6-7" stroke="#231f20" stroke-width="2.2" fill="none"/></svg>FIRST AID CERTIFIED</li>
    <li><svg viewBox="0 0 18 18"><circle cx="9" cy="9" r="8" fill="#a9cc7a"/><path d="M4.5 9.5l3 3 6-7" stroke="#231f20" stroke-width="2.2" fill="none"/></svg>EXPERIENCED IN DOG WALKING,<br>DOG GROUP BEHAVIOUR &amp; TRAINING.</li>
    <li><svg viewBox="0 0 18 18"><circle cx="9" cy="9" r="8" fill="#a9cc7a"/><path d="M4.5 9.5l3 3 6-7" stroke="#231f20" stroke-width="2.2" fill="none"/></svg>RELIABLE AND WALK DURING RAIN,<br>SNOW AND YES, EVEN SUN!</li>
  </ul>

  <div class="footer-stripe"></div>
  <div class="footer-band"></div>

  <p class="brand-name">TALLOWBROOK <span class="accent">PAWS</span></p>
  <p class="tagline">Licensed |&nbsp; Insured &nbsp;| Pawfessional</p>
  <p class="call">CALL NOW : 604-555-0148</p>
  <p class="website">WWW.TALLOWBROOKPAWS.COM</p>

  <div class="logo">
    <span class="logo-mark"></span>
    <span class="logo-name">TALLOWBROOK PAWS</span>
  </div>

  <div class="seal">
    <svg viewBox="0 0 230 230" width="230" height="230">
      <polygon fill="#ffffff" points="115,2 129,17 147,7 155,26 175,22 177,42 197,43 193,63 211,71 201,88 216,101 201,115 216,129 201,142 211,159 193,167 197,187 177,188 175,208 155,204 147,223 129,213 115,228 101,213 83,223 75,204 55,208 53,188 33,187 37,167 19,159 29,142 14,129 29,115 14,101 29,88 19,71 37,63 33,43 53,42 55,22 75,26 83,7 101,17"/>
      <polygon fill="#acd036" points="115,12 127,25 143,17 150,33 168,30 170,47 187,49 184,66 199,73 191,88 204,99 191,115 204,131 191,142 199,157 184,164 187,181 170,183 168,200 150,197 143,213 127,205 115,218 103,205 87,213 80,197 62,200 60,183 43,181 46,164 31,157 39,142 26,131 39,115 26,99 39,88 31,73 46,66 43,49 60,47 62,30 80,33 87,17 103,25"/>
    </svg>
    <div class="seal-text"><span class="small">FIRST</span><span class="small">WALK</span><span class="big">FREE</span></div>
  </div>
</main>
</body>
</html>
```